BLUE HAVEN (Business Card for Training Company)

Blue Haven is a training and consultancy company with a focus on executive protection and medical. I would like the card to be nice and sharp, not overdone and in black and red. I would also like it to highlight that it is "A Dravin Company"

I would like it to be simple and highlight a few things.

1. Name
2. Title
3. Phone Number
4. Email

I would also like www.dravinholdings.example/blue-haven to be on the card somewhere.

Target Market(s)

Security Companies

Industry/Entity Type

Security

Contact Information for Business Card

Blue Haven is a training and consultancy company with a focus on executive protection and medical. I would like the card to be nice and sharp, not overdone and in black and red. I would also like it to highlight that it is "A Dravin Company" I would like it to be simple and highlight a few things. 1. Name 2. Title 3. Phone Number 4. Email I would also like www.dravinholdings.example/blue-haven to be on the card somewhere.

Requirements
Must have
• A Dravin Company listed on the card and the website
Nice to have
• Highlight Medical Training, Consultancy & Executive Protection Courses

```html
<!DOCTYPE html>
<html lang="en">
<head>
<meta charset="utf-8">
<title>Blue Haven — Business Card</title>
<link rel="stylesheet" href="https://fonts.googleapis.com/css2?family=Open+Sans:ital,wght@0,400;0,700;0,800;1,400&display=swap">
<style>
  :root {
    --brand-red: #6a0e0e;
    --brand-red-light: #8a1c1c;
    --ink: #111111;
    --text-grey: #555555;
    --paper: #ffffff;
    --backdrop: #2a2a2a;
  }
  * { box-sizing: border-box; margin: 0; padding: 0; }
  html, body {
    width: 1200px; height: 900px; overflow: hidden;
    background: var(--backdrop);
    font-family: "Open Sans", Arial, sans-serif;
  }
  .stage {
    width: 1200px; height: 900px;
    display: flex; flex-direction: column; align-items: center; justify-content: center;
    gap: 40px;
  }
  .card {
    position: relative;
    width: 630px; height: 360px;
    overflow: hidden;
    box-shadow: 0 14px 30px rgba(0,0,0,.55);
  }

  /* Front */
  .card-front { background: var(--paper); }
  .front-wave { position: absolute; inset: 0; width: 100%; height: 100%; }
  .wordmark {
    font-weight: 800; line-height: .92; letter-spacing: 1px; text-transform: uppercase;
  }
  .card-front .wordmark {
    position: absolute; left: 46px; top: 62px;
    font-size: 54px; color: var(--ink);
  }
  .divider {
    position: absolute; left: 318px; top: 92px;
    width: 1.5px; height: 118px; background: var(--brand-red);
  }
  .contact {
    position: absolute; left: 340px; top: 94px;
    color: var(--text-grey); font-size: 16px;
  }
  .contact-name {
    color: var(--brand-red); font-weight: 800; font-size: 22px;
    letter-spacing: .5px; text-transform: uppercase;
  }
  .contact-title { font-size: 17px; margin-bottom: 12px; }
  .contact-line { display: flex; align-items: center; gap: 8px; line-height: 1.6; }
  .contact-line svg { width: 13px; height: 13px; fill: var(--brand-red); flex: none; }
  .front-url {
    position: absolute; left: 26px; bottom: 26px;
    color: var(--paper); font-size: 14px; letter-spacing: .3px;
  }

  /* Back */
  .card-back { background: var(--brand-red); color: var(--paper); }
  .card-back .wordmark {
    position: absolute; right: 50px; top: 44px;
    font-size: 66px; color: var(--paper); text-align: left;
  }
  .back-parent {
    position: absolute; left: 190px; bottom: 74px;
    font-weight: 800; font-size: 15px; letter-spacing: .5px; text-transform: uppercase;
  }
  .back-services {
    position: absolute; left: 40px; right: 40px; bottom: 40px;
    font-size: 15px; letter-spacing: .3px; text-align: center;
  }
</style>
</head>
<body>
<main class="stage">

  <section class="card card-front" aria-label="Business card front">
    <svg class="front-wave" viewBox="0 0 630 360" preserveAspectRatio="none" aria-hidden="true">
      <path d="M0,214 C160,222 270,270 360,310 C430,340 500,356 560,360 L0,360 Z" fill="var(--ink)"/>
      <path d="M0,222 C160,230 265,278 350,316 C420,346 490,360 540,360 L0,360 Z" fill="var(--paper)"/>
      <path d="M0,228 C160,236 260,284 340,320 C410,350 470,360 510,360 L0,360 Z" fill="var(--brand-red)"/>
      <path d="M0,228 C90,232 150,244 200,258" fill="none" stroke="var(--brand-red-light)" stroke-width="6" opacity=".7"/>
    </svg>

    <div class="wordmark">Blue<br>Haven</div>
    <div class="divider"></div>

    <div class="contact">
      <p class="contact-name">Dorian Vell</p>
      <p class="contact-title">President</p>
      <p class="contact-line">
        <svg viewBox="0 0 24 24"><path d="M6.6 10.8a15.1 15.1 0 0 0 6.6 6.6l2.2-2.2a1 1 0 0 1 1-.25 11.4 11.4 0 0 0 3.6.57 1 1 0 0 1 1 1V20a1 1 0 0 1-1 1A17 17 0 0 1 3 4a1 1 0 0 1 1-1h3.5a1 1 0 0 1 1 1c0 1.25.2 2.46.57 3.6a1 1 0 0 1-.25 1z"/></svg>
        555-014-2290
      </p>
      <p class="contact-line">
        <svg viewBox="0 0 24 24"><path d="M2 5h20v2l-10 6L2 7zm0 4 10 6 10-6v10H2z"/></svg>
        info@dravinholdings.example
      </p>
    </div>

    <p class="front-url">www.dravinholdings.example/blue-haven</p>
  </section>

  <section class="card card-back" aria-label="Business card back">
    <div class="wordmark">Blue<br>Haven</div>
    <p class="back-parent">A Dravin Company</p>
    <p class="back-services">Medical Training &bull; Consultancy &bull; Executive Protection Courses</p>
  </section>

</main>
</body>
</html>
```